Qarv Processing

I need this business card to look exactly like a credit card.
with chip on front and stripe on back as well
I want my cell phone number to be the "credit card number that goes across the front.

Front:
(The name of my company is) QARV
Marcus Bindle
National Sales Director
Cell: 505 218 6937

Back:
Fax: 877 6152948
24/7 Support: 800 627 3154
Marcuskbindle@quellmail.example
Cash Discount 0% Fees
Free Equipment
No Contracts
No Hidden Fees

```html
<!DOCTYPE html>
<html lang="en">
<head>
<meta charset="utf-8">
<title>Qarv Processing – Business Card</title>
<link rel="stylesheet" href="https://fonts.googleapis.com/css2?family=Poppins:wght@300;400;500;600;700&display=swap">
<style>
  :root {
    --page-bg: #e8e8ea;
    --card-blue: #043f7a;
    --accent-blue: #1884c6;
    --chip-gold: #cdc544;
    --chip-line: #f4f0c8;
    --white: #ffffff;
    --ink: #0b0b0f;
    --stripe: #050505;
  }
  * { box-sizing: border-box; margin: 0; padding: 0; }
  html, body {
    width: 1200px; height: 1200px; overflow: hidden;
    background: var(--page-bg);
    font-family: "Poppins", sans-serif;
  }
  .canvas {
    width: 1200px; height: 1200px;
    display: flex; flex-direction: column;
    align-items: center; justify-content: center; gap: 70px;
  }
  .card {
    position: relative;
    width: 820px; height: 517px;
    border-radius: 30px;
    background: var(--card-blue);
    overflow: hidden;
  }
  /* front */
  .card-front .accent-curve { position: absolute; inset: 0; }
  .brand-name {
    position: absolute; top: 44px; right: 66px;
    color: var(--white); font-weight: 300; font-size: 30px; letter-spacing: 1px;
  }
  .contactless-mark { position: absolute; left: 86px; top: 282px; }
  .chip { position: absolute; left: 138px; top: 270px; }
  .card-number {
    position: absolute; left: 150px; top: 372px;
    color: var(--white); font-weight: 600; font-size: 36px; word-spacing: 18px;
  }
  .holder { position: absolute; left: 200px; top: 430px; color: var(--white); }
  .holder-name { font-weight: 700; font-size: 32px; line-height: 1.1; }
  .holder-title { font-weight: 500; font-size: 15px; letter-spacing: 0.3px; }
  /* back */
  .mag-stripe {
    position: absolute; left: 0; right: 0; top: 62px; height: 96px;
    background: var(--stripe);
  }
  .contact-block {
    position: absolute; left: 96px; top: 290px;
    color: var(--ink); font-size: 20px; line-height: 1.55;
  }
  .contact-heading { font-weight: 700; font-size: 22px; text-decoration: underline; }
  .benefits-list {
    position: absolute; right: 86px; top: 255px;
    list-style: none; color: var(--ink); font-size: 20px; line-height: 1.55;
  }
</style>
</head>
<body>
<main class="canvas">

  <section class="card card-front" aria-label="Card front">
    <svg class="accent-curve" width="820" height="517" viewBox="0 0 820 517">
      <path d="M452 0 L502 0 Q548 250 512 517 L498 517 Q520 250 452 0 Z" fill="var(--accent-blue)"/>
    </svg>
    <div class="brand-name">QARV</div>
    <svg class="contactless-mark" width="60" height="80" viewBox="0 0 60 80">
      <path d="M20 4 L4 66 L56 74 Z" fill="none" stroke="var(--white)" stroke-width="4" stroke-linejoin="round"/>
    </svg>
    <svg class="chip" width="106" height="74" viewBox="0 0 106 74">
      <rect x="0" y="0" width="106" height="74" rx="16" fill="var(--chip-gold)"/>
      <g stroke="var(--chip-line)" stroke-width="3" fill="none">
        <line x1="0" y1="25" x2="34" y2="25"/>
        <line x1="0" y1="49" x2="34" y2="49"/>
        <line x1="72" y1="25" x2="106" y2="25"/>
        <line x1="72" y1="49" x2="106" y2="49"/>
        <rect x="34" y="16" width="38" height="42" rx="6"/>
        <line x1="53" y1="0" x2="53" y2="16"/>
        <line x1="53" y1="58" x2="53" y2="74"/>
      </g>
    </svg>
    <div class="card-number">505 218 6937</div>
    <div class="holder">
      <div class="holder-name">MARCUS BINDLE</div>
      <div class="holder-title">NATIONAL SALES DIRECTOR</div>
    </div>
  </section>

  <section class="card card-back" aria-label="Card back">
    <div class="mag-stripe"></div>
    <div class="contact-block">
      <div class="contact-heading">CONTACT US:</div>
      <div>Fax: 877 6152948</div>
      <div>24/7 Support: 800 627 3154</div>
      <div>Marcuskbindle@quellmail.example</div>
    </div>
    <ul class="benefits-list">
      <li>Cash Discount 0% Fees</li>
      <li>Free Equipment</li>
      <li>No Contracts</li>
      <li>No Hidden Fees</li>
    </ul>
  </section>

</main>
</body>
</html>
```